TRLcraftwork Permanent Makeup Artisan - Owner/Operator

Id like my card to present my qualitative, creative, modern & professional work in the Beauty industry. Being a male and in this line of work I need to come across as the best in my field. I am a passionate person and love what I do. I work hard, travel far, actively connect with my clients and go the extra mile. I'm associated with LuminoraClinics all over SA and my clients get refered to my via word of mouth. Doctors and other professionals in the Beauty industry talk about my qualitative work and ethics. Thus my business card needs to represent this image and standard of work.

Target Market(s)

Woman 20-70 yr old

Industry/Entity Type

Industry

Contact Information for Business Card

Pieter Vosloo
Permanent Makeup Artisan
+27 (0) 71 482 9053
info@TRLcraftwork.example
www.TRLcraftwork.example

Font styles to use
Other font styles liked:
• Brannball, Bell MT, Arial

Colors
feeeee

Requirements
Must have
• Small logos of the social media sites I'm visible on.
• A short discription of my experience and what I do now with the current services I offer, perhaps.
Should not have
• Look cluttered nor to much

```html
<!DOCTYPE html>
<html lang="en">
<head>
<meta charset="utf-8">
<title>TRLcraftwork – Business Card</title>
<link rel="stylesheet" href="https://fonts.googleapis.com/css2?family=Open+Sans:wght@400;600&display=swap">
<style>
  :root {
    --page-bg: #e6e7ea;
    --card-bg: #fbfbfc;
    --card-edge: #d9dadf;
    --ink: #1e1e22;
    --brand-teal: #4a9ea3;
    --accent-purple: #7a63a8;
    --bullet: #6e6394;
    --band-start: #c9d6e6;
    --band-mid: #b8b1dc;
    --band-end: #6f5fae;
  }
  * { box-sizing: border-box; margin: 0; padding: 0; }
  html, body {
    width: 1200px; height: 970px; overflow: hidden;
    background: var(--page-bg);
    font-family: "Open Sans", Arial, sans-serif;
    color: var(--ink);
  }
  .business-card {
    position: absolute; left: 60px; top: 185px;
    width: 1080px; height: 600px;
    background: var(--card-bg);
    border: 1px solid var(--card-edge);
    border-radius: 30px;
    overflow: hidden;
    box-shadow: 0 10px 30px rgba(0,0,0,0.08);
  }
  .brand { position: absolute; left: 54px; top: 40px; }
  .brand-name {
    font-size: 78px; font-weight: 600; line-height: 1;
    color: var(--brand-teal); letter-spacing: -1px;
  }
  .brand-tagline {
    margin-top: 22px; margin-left: 34px;
    font-size: 14px; font-weight: 600; letter-spacing: 1px;
  }
  .about {
    position: absolute; left: 54px; top: 268px;
    font-size: 24px; line-height: 31px; width: 500px;
  }
  .services {
    position: absolute; left: 54px; top: 370px;
    list-style: none; font-size: 24px; line-height: 31px;
  }
  .services li::before, .service-inline::before {
    content: ""; display: inline-block;
    width: 9px; height: 9px; border-radius: 50%;
    background: var(--bullet); margin: 0 6px 4px 0;
  }
  .service-inline { margin-left: 10px; }
  .contact {
    position: absolute; right: 53px; top: 182px; text-align: right;
  }
  .person-name { font-size: 31px; font-weight: 600; color: var(--accent-purple); line-height: 36px; }
  .person-role { font-size: 23px; line-height: 30px; }
  .contact-lines { margin-top: 58px; font-size: 23px; line-height: 36px; }
  .social-handle {
    margin-top: 10px; font-size: 23px;
    display: flex; align-items: center; justify-content: flex-end; gap: 10px;
  }
  .social-dot { width: 24px; height: 24px; border-radius: 50%; background: var(--accent-purple); }
  .footer-band {
    position: absolute; left: 0; bottom: 0; width: 100%; height: 108px;
    background: linear-gradient(90deg, var(--band-start) 25%, var(--band-mid) 60%, var(--band-end) 100%);
  }
  .eye-artwork {
    position: absolute; left: 0; top: 0; width: 360px; height: 100%;
    background: linear-gradient(90deg, #3c4f86 0%, #5a7fb2 30%, #8a6bb5 60%, rgba(201,214,230,0) 100%);
  }
</style>
</head>
<body>
  <main class="business-card">
    <header class="brand">
      <div class="brand-name">TRLcraftwork</div>
      <div class="brand-tagline">MAKEUP ARTIST . CONSULTANT . BROW ARTISAN</div>
    </header>

    <p class="about">Professional Makeup Artist, Can transform any woman, according to her style, mood, or the occasion.</p>

    <ul class="services">
      <li>Eyebrow &amp; Eyeliner Embroidery</li>
      <li>Wedding Day Makeup <span class="service-inline">Makeup Lesson</span></li>
      <li>Eyebrow Grooming and more ....</li>
    </ul>

    <section class="contact">
      <div class="person-name">Pieter Vosloo</div>
      <div class="person-role">Permanent Makeup Artisan</div>
      <div class="contact-lines">
        <div>+27 (0) 71 482 9053</div>
        <div>info@TRLcraftwork.example</div>
        <div>www.TRLcraftwork.example</div>
      </div>
      <div class="social-handle"><span class="social-dot"></span>TRLcraftwork</div>
    </section>

    <div class="footer-band">
      <div class="eye-artwork" role="img" aria-label="Close-up of an eye with long lashes and colourful blue and purple eye makeup"></div>
    </div>
  </main>
</body>
</html>
```